Graphic Banner Design - 2.5' x 6' - High Tech Company

We are in need of a banner design for an outdoor sign that will be used at sponsorship events.

Size
2.5' x 6'

The company is a high tech company, and the design will be used for action sports events. So lining up to that would be good.

Tag line to be incorporated...
"Extreme IT Services for Extreme Needs."

Target Market(s)

Business Owners, Entrepreneurs, IT Professionals.

Industry/Entity Type

Information Technology

Logo Text

Vexlora

Colors

Designer to choose colors to be used in the design.

Requirements
Must have
• Must feel young and vibrant, fit in to an action sports event and just be out of this world awesome.
• In the world of the IT, we are the Zanverolli. Fast, Awesome, not necessarily cheap, but you know it will do what you want extremely well. Not for everyone, but always desired.

```html
<!DOCTYPE html>
<html lang="en">
<head>
<meta charset="utf-8">
<title>Vexlora – Event Banners</title>
<link href="https://fonts.googleapis.com/css2?family=Lato:wght@400;700&family=Kaushan+Script&family=Montserrat:wght@400&family=Oswald:wght@300;400&display=swap" rel="stylesheet">
<style>
  :root {
    --page: #ffffff;
    --navy: #141a2b;
    --navy-deep: #0c1120;
    --ring: rgba(255,255,255,0.035);
    --gold: #f6c945;
    --gold-deep: #f2a81c;
    --white: #ffffff;
    --periwinkle: #8d98d0;
    --bulb: #5b7de0;
    --photo-a: #3a4a78;
    --photo-b: #7d87a6;
  }
  * { margin: 0; padding: 0; box-sizing: border-box; }
  html, body { width: 1200px; height: 1000px; overflow: hidden; background: var(--page); }
  .canvas { position: relative; width: 1200px; height: 1000px; }

  .banner { position: absolute; left: 106px; width: 983px; height: 409px; overflow: hidden; }
  .banner--stars { top: 77px; background: var(--navy); }
  .banner--crowd { top: 524px; background: linear-gradient(90deg, var(--navy-deep), var(--navy)); }
  .banner svg.backdrop { position: absolute; inset: 0; }

  .brand-top {
    position: absolute; left: 356px; top: 118px;
    font-family: "Lato", sans-serif; font-weight: 700; font-size: 54px;
    color: var(--gold); letter-spacing: 1px; line-height: 1;
  }
  .script-title {
    position: absolute; left: 348px; top: 180px;
    font-family: "Kaushan Script", cursive; font-size: 36px;
    color: var(--gold-deep); line-height: 1;
  }
  .tagline-top {
    position: absolute; left: 350px; top: 238px;
    font-family: "Lato", sans-serif; font-size: 23px; color: var(--white);
  }

  .brand-bottom {
    position: absolute; left: 50px; top: 180px;
    font-family: "Montserrat", sans-serif; font-size: 24px; color: var(--white);
  }
  .headline {
    position: absolute; left: 50px; top: 224px;
    font-family: "Oswald", sans-serif; font-weight: 400; font-size: 44px; line-height: 1;
    background: linear-gradient(90deg, var(--periwinkle), var(--white));
    -webkit-background-clip: text; background-clip: text; color: transparent;
  }
  .tagline-bottom {
    position: absolute; left: 50px; top: 276px;
    font-family: "Oswald", sans-serif; font-weight: 300; font-size: 26px; color: var(--white);
  }
</style>
</head>
<body>
<main class="canvas">

  <section class="banner banner--stars">
    <svg class="backdrop" width="983" height="409" viewBox="0 0 983 409">
      <circle cx="168" cy="212" r="250" fill="var(--ring)"/>
      <circle cx="168" cy="212" r="180" fill="var(--ring)"/>
      <circle cx="168" cy="212" r="120" fill="var(--ring)"/>
      <g role="img" aria-label="Light bulb inside a starburst illustration">
        <circle cx="218" cy="215" r="108" fill="#1f2a4a"/>
        <circle cx="218" cy="205" r="62" fill="var(--bulb)" opacity="0.7"/>
      </g>
      <circle role="img" aria-label="Email envelope icon" cx="84" cy="45" r="22" fill="#2a3556"/>
      <circle role="img" aria-label="Plug with leaves icon" cx="42" cy="245" r="22" fill="#2a3556"/>
      <circle role="img" aria-label="Cloud icon" cx="14" cy="352" r="22" fill="#2a3556"/>
      <circle role="img" aria-label="Satellite dish icon" cx="690" cy="85" r="30" fill="#2a3556"/>
      <circle role="img" aria-label="Rocket icon" cx="890" cy="150" r="44" fill="#3a3a3a" opacity="0.6"/>
      <circle role="img" aria-label="Computer with mouse icon" cx="575" cy="320" r="32" fill="#2a3556"/>
      <circle role="img" aria-label="Telescope on tripod icon" cx="845" cy="345" r="40" fill="#2a3556"/>
    </svg>
    <div class="brand-top">Vexlora</div>
    <div class="script-title">High Tech Company</div>
    <div class="tagline-top">Extreme IT Services for Extreme Needs</div>
  </section>

  <section class="banner banner--crowd">
    <svg class="backdrop" width="983" height="409" viewBox="0 0 983 409">
      <defs>
        <linearGradient id="crowdTone" x1="0" y1="0" x2="0" y2="1">
          <stop offset="0" stop-color="var(--photo-b)"/>
          <stop offset="1" stop-color="var(--photo-a)"/>
        </linearGradient>
      </defs>
      <circle cx="790" cy="230" r="590" fill="none" stroke="var(--ring)" stroke-width="70"/>
      <circle cx="790" cy="230" r="480" fill="none" stroke="var(--ring)" stroke-width="50"/>
      <circle role="img" aria-label="Concert crowd with raised hands under stage lights" cx="800" cy="222" r="385" fill="url(#crowdTone)"/>
    </svg>
    <div class="brand-bottom">Vexlora</div>
    <div class="headline">HIGH TECH COMPANY</div>
    <div class="tagline-bottom">Extreme IT Services for Extreme Needs</div>
  </section>

</main>
</body>
</html>
```